Flyer-Design für Einzelhandel/Online-Shop für Werbetechnikzubehör
Zielgruppe
Wir sind ein Einzelhandel / Onlineshop für Werbetechnikzubehör. Plotterfolie, Plotter, DIY-Artikel. Wir kommen mitten aus dem Ruhrgebiet und unser Name verbindet das Plotten und unsere Herkunft. „Falzwerkstück“
Unsere Zielgruppe sind Kreative aus dem Bastel- / Nähbereich.
Aufgabenstellung
Wir legen wert auf die Verbindung zum Ruhrgebiet (Zechen und co.) Anbei stellen wir auch eine Datei zur Verfügung, die bereits auf unserem Auto und Gutscheinen implementiert ist. Gerne darf diese genutzt werden.
Wir legen Wert auf Gradlinigkeit und Übersichtlichkeit.
Unser Flyer soll ein A6 Format sein (Datenformat: 154 x 111 mm
3 mm Beschnitt) diesen wir mit einem Rabattcode versehen wollen.
Des Weiteren benötigen wir auch die Abbidung von Instagram / Facebook / Homepage.
Daher benötigen wir das Design natürlich auch in einem Bearbeitungsmodus für ai.
Gerade die Felder Rabattcode und Gutscheinbedingungen sollten beachtet werden.
10% auf alle Vinyl, Flex & Flockfolie (Bogenware)
Der Flyer wird als Versandbeileger für befreundete Unternehmen benötigt.
Wir möchten mit diesem Flyer Neukunden gewinnen.
Der Flyer kann beidseitig gestaltet werden. Hoch oder Quer ist auch frei wählbar.
Unsere Farben sind als Datei hochgeladen.

```html
<!DOCTYPE html>
<html lang="de">
<head>
<meta charset="utf-8">
<title>Falzwerkstück – Neukundenrabatt Flyer</title>
<link href="https://fonts.googleapis.com/css2?family=Roboto:wght@300;400;500&display=swap" rel="stylesheet">
<style>
  :root {
    --teal: #5499a9;
    --dark: #555555;
    --ink: #4a4a4a;
    --body-text: #666666;
    --paper: #ffffff;
    --stage: #f2f2f2;
    --skyline-dark: #5a5a5a;
    --skyline-faint: #dadada;
  }
  * { box-sizing: border-box; margin: 0; padding: 0; }
  html, body { width: 1140px; height: 1200px; overflow: hidden; }
  body {
    background: var(--stage);
    font-family: "Roboto", Arial, sans-serif;
    position: relative;
  }
  .flyer {
    position: absolute;
    top: 422px;
    width: 504px;
    height: 358px;
    background: var(--paper);
    box-shadow: 0 1px 5px rgba(0,0,0,0.25);
    overflow: hidden;
  }
  .flyer--front { left: 52px; }
  .flyer--back { left: 584px; }
  .footer-band {
    position: absolute; left: 0; right: 0; bottom: 0; height: 19px;
    background: var(--dark);
  }

  /* Front */
  .skyline {
    position: absolute; left: 12px; right: 12px; top: 35px; height: 82px;
    background: linear-gradient(to bottom, #ededed 0%, #a9a9a9 45%, var(--skyline-dark) 100%);
  }
  .skyline-base {
    position: absolute; left: 12px; right: 12px; top: 117px; height: 3px;
    background: var(--dark);
  }
  .title-band {
    position: absolute; left: 0; right: 0; top: 134px; height: 32px;
    background: var(--teal);
    color: #fff; font-weight: 400; font-size: 24px; letter-spacing: 0.5px;
    text-align: center; line-height: 32px;
  }
  .title-rule {
    position: absolute; left: 0; right: 0; top: 173px; height: 1px;
    background: var(--dark);
  }
  .brand-name-front {
    position: absolute; left: 0; right: 0; top: 268px;
    text-align: center; font-weight: 300; font-size: 36px; line-height: 40px;
    color: var(--ink);
  }

  /* Back */
  .skyline--faint {
    left: 166px; right: 20px; top: 18px; height: 58px;
    background: linear-gradient(to bottom, #f6f6f6, var(--skyline-faint));
  }
  .brand-name-back {
    position: absolute; left: 19px; top: 58px;
    color: var(--teal); font-size: 15px; font-weight: 400;
  }
  .brand-rule {
    position: absolute; left: 19px; right: 19px; top: 80px; height: 2px;
    background: var(--teal);
  }
  .headline {
    position: absolute; right: 23px; top: 87px;
    color: var(--teal); font-size: 23px; font-weight: 400; line-height: 26px;
  }
  .field {
    position: absolute; left: 19px; width: 172px;
    color: var(--teal); font-size: 14px; font-weight: 400; line-height: 16px;
  }
  .field::after {
    content: ""; position: absolute; left: 0; right: 0; top: 36px; height: 1px;
    background: var(--teal);
  }
  .field--code { top: 140px; }
  .field--date { top: 197px; }
  .terms {
    position: absolute; left: 264px; top: 140px; width: 220px;
    color: var(--body-text); font-size: 9.8px; line-height: 11.6px; font-weight: 300;
  }
  .terms h3 { font-size: 11px; font-weight: 400; color: var(--ink); line-height: 14px; margin-bottom: 10px; }
  .terms p { margin-bottom: 11px; }
  .contact {
    position: absolute; right: 28px; top: 302px;
    display: flex; align-items: center; gap: 8px;
    color: var(--ink); font-size: 12.5px; font-weight: 400;
  }
  .contact .sep { margin: 0 1px; }
  .social-square {
    width: 21px; height: 21px; background: var(--dark); border-radius: 2px;
  }
</style>
</head>
<body>

  <section class="flyer flyer--front">
    <div class="skyline" role="img" aria-label="Skyline des Ruhrgebiets: Achterbahn, Hochhaus, Tetraeder-Halde, Zechen-Fördertürme, Schornstein, Windrad, Förderwagen mit Schlägel und Eisen, Fernsehturm und U-Turm"></div>
    <div class="skyline-base"></div>
    <div class="title-band">NEUKUNDENRABATT</div>
    <div class="title-rule"></div>
    <div class="brand-name-front">FALZWERKSTÜCK</div>
    <div class="footer-band"></div>
  </section>

  <section class="flyer flyer--back">
    <div class="skyline skyline--faint" role="img" aria-label="Blasse Skyline des Ruhrgebiets mit Zechen-Fördertürmen, Halde, Windrad und Fernsehturm"></div>
    <div class="brand-name-back">Falzwerkstück</div>
    <div class="brand-rule"></div>
    <h2 class="headline">NEUKUNDENRABATT</h2>

    <div class="field field--code">RABATT-CODE</div>
    <div class="field field--date">DATUM</div>

    <div class="terms">
      <h3>Bedingungen:</h3>
      <p>Lorem ipsum dolor sit amet, consectetuer adipiscing elit, sed diam nonummy nibh euismod incidunt ut laoreet dolore magna aliquam erat volutpat.</p>
      <p>Ut wisi enim ad minim veniam, quis nostrud exerci tation ullamcorper suscipit lobortis nisl ut aliquip ex ea commodo consequat. Duis autem vel eum iriure dolor in.</p>
    </div>

    <div class="contact">
      <span>Kesselstr. 42</span><span class="sep">|</span>
      <span>45127 Essen</span><span class="sep">|</span>
      <span>www.falzwerkstueck.de</span>
      <span class="social-square" aria-hidden="true"></span>
      <span class="social-square" aria-hidden="true"></span>
    </div>
    <div class="footer-band"></div>
  </section>

</body>
</html>
```